Word Template for KESTREL Polls

KESTREL Polls stands for 'Kinship Evaluation Study Tracking Regional Everyday Lives Polls'. It is a collaborative research effort to format and combine multiple sources of public opinion data from around the world into merged datasets. We need a Microsoft Word template design for our research reports, dataset codebooks, crowdsourced development guidelines, and other documents that will be produced as part of the research and development. The template should match the website design and logo, which are attached to this contest (these are the files from previous successful design contests).

The main purpose will be to write reports discussing research and analysis. There will be lots data visualizations (bar charts, scatter plots, pie charts, histograms, trend line charts etc.) as well as tables, diargams, and photos mixed in wit all the text. A second purpose will be to write guidebooks to describe processes and teach others how to manage data, find variables, and write code, which will include screenshots and Word are diagrams and figures.

There are some document uploaded as examples for the kinds of things for which we need the template (working papers, codebooks, pamphlets, etc)

Target Market(s)

academia, government, non-profits, postgraduates, researchers

Font styles to use
Serif

Colors

Designer to choose colors to be used in the design.

Requirements
Must have
• A4 size page template
• Cover page
• Must match website design and logo (see attached)
Nice to have
• Colors to match logo and website (see attached)

```html
<!DOCTYPE html>
<html lang="en">
<head>
<meta charset="utf-8">
<title>KESTREL Polls – Report Template</title>
<link rel="stylesheet" href="https://fonts.googleapis.com/css2?family=Roboto:wght@400;500&display=swap">
<style>
  :root {
    --blue-deep: #1b6fbd;
    --blue-bright: #22a5df;
    --band-blue: #21a6e0;
    --label-grey: #6b6b6b;
    --text-grey: #5e5e5e;
    --white: #ffffff;
  }
  * { margin: 0; padding: 0; box-sizing: border-box; }
  html, body { width: 834px; height: 1200px; overflow: hidden; background: var(--white); }
  body { font-family: "Roboto", Arial, sans-serif; position: relative; }

  .cover-header {
    position: absolute; left: 0; top: 0; width: 834px; height: 331px;
    background: linear-gradient(100deg, var(--blue-deep) 0%, #1d8fd4 55%, var(--blue-bright) 100%);
    overflow: hidden;
  }
  .header-artwork {
    position: absolute; left: 0; top: 16px; width: 224px; height: 296px;
    background: radial-gradient(ellipse at 60% 50%, rgba(90,230,255,0.45) 0%, rgba(40,170,230,0.15) 55%, rgba(30,120,200,0) 80%);
  }
  .header-glow {
    position: absolute; right: -40px; top: -20px; width: 320px; height: 360px;
    background: radial-gradient(circle at 60% 40%, rgba(255,255,255,0.12), rgba(255,255,255,0) 65%);
  }
  .report-title {
    position: absolute; left: 270px; top: 120px; width: 540px;
    color: var(--white); font-weight: 500; font-size: 30px; line-height: 40px;
  }

  .section { position: absolute; left: 0; width: 834px; }
  .section--light { background: var(--white); }
  .section--blue { background: var(--band-blue); }

  .section-label {
    position: absolute; height: 48px; line-height: 48px;
    font-size: 23px; font-weight: 400; letter-spacing: 0.2px; text-transform: uppercase;
  }
  .section--light .section-label { left: 0; background: var(--label-grey); color: var(--white); padding: 0 22px 0 42px; }
  .section--blue .section-label { right: 0; background: var(--white); color: var(--text-grey); padding: 0 40px 0 29px; }

  .section-body {
    position: absolute; left: 41px; width: 752px;
    font-size: 17.5px; line-height: 22.8px; font-weight: 500;
  }
  .section--light .section-body { color: var(--text-grey); }
  .section--blue .section-body { color: var(--white); }
</style>
</head>
<body>
  <header class="cover-header">
    <div class="header-artwork" role="img" aria-label="Illustration of a digital network profile in glowing cyan dots"></div>
    <div class="header-glow"></div>
    <h1 class="report-title">Kinship Evaluation Study Tracking Regional Everyday Lives Polls</h1>
  </header>

  <section class="section section--light" style="top:331px; height:218px;">
    <h2 class="section-label" style="top:27px;">Introduction</h2>
    <p class="section-body" style="top:92px;">Lorem ipsum dolor sit amet, consectetuer adipiscing elit, sed diam nonummy nibh euismod tincidunt ut laoreet dolore magna aliquam erat volutpat. Ut wisi enim ad minim veniam, quis nostrud exerci tation ullamcorper suscipit lobortis nisl ut aliquip ex ea commodo consequat. Duis autem vel eum iriure dolor in hendrerit in vulputate velit esse</p>
  </section>

  <section class="section section--blue" style="top:549px; height:217px;">
    <h2 class="section-label" style="top:27px;">Method</h2>
    <p class="section-body" style="top:92px;">Lorem ipsum dolor sit amet, consectetuer adipiscing elit, sed diam nonummy nibh euismod tincidunt ut laoreet dolore magna aliquam erat volutpat. Ut wisi enim ad minim veniam, quis nostrud exerci tation ullamcorper suscipit lobortis nisl ut aliquip ex ea commodo consequat. Duis autem vel eum iriure dolor in hendrerit in vulputate velit esse</p>
  </section>

  <section class="section section--light" style="top:766px; height:216px;">
    <h2 class="section-label" style="top:26px;">Results</h2>
    <p class="section-body" style="top:91px;">Lorem ipsum dolor sit amet, consectetuer adipiscing elit, sed diam nonummy nibh euismod tincidunt ut laoreet dolore magna aliquam erat volutpat. Ut wisi enim ad minim veniam, quis nostrud exerci tation ullamcorper suscipit lobortis nisl ut aliquip ex ea commodo consequat. Duis autem vel eum iriure dolor in hendrerit in vulputate velit esse</p>
  </section>

  <section class="section section--blue" style="top:982px; height:218px;">
    <h2 class="section-label" style="top:28px;">Discussion</h2>
    <p class="section-body" style="top:92px;">Lorem ipsum dolor sit amet, consectetuer adipiscing elit, sed diam nonummy nibh euismod tincidunt ut laoreet dolore magna aliquam erat volutpat. Ut wisi enim ad minim veniam, quis nostrud exerci tation ullamcorper suscipit lobortis nisl ut aliquip ex ea commodo consequat. Duis autem vel eum iriure dolor in hendrerit in vulputate velit esse</p>
  </section>
</body>
</html>
```